We are having a Bright Dawn, Bold Self Reshape Challenge at our fitness studio. We need a poster design using the template attached as a reference. I have also included our Vorabloom logo to put on the poster. Please DO NOT use the graphics in the flyer as we are expecting something much better :-)

-Size needed 11x17 with bleeding for printing

-We need this made in Photoshop (CS3 friendly) or at least delivered in PS as we might change some text or re-arrange the design later on.

-We need this in layers.

```html
<!DOCTYPE html>
<html lang="en">
<head>
<meta charset="utf-8">
<title>Bright Dawn, Bold Self Reshape Challenge</title>
<link rel="stylesheet" href="https://fonts.googleapis.com/css2?family=Oswald:wght@300;600;700&family=Nunito:wght@800;900&display=swap">
<style>
  :root {
    --title-red: #e0262b;
    --ink-blue: #233a8f;
    --box-red: #ec2027;
    --sun-yellow: #f6ec1c;
    --band-red: #e5232a;
    --white: #ffffff;
    --sky-top: #f4e6c6;
    --sky-mid: #f2b84e;
    --sky-low: #c8661d;
  }
  * { margin: 0; padding: 0; box-sizing: border-box; }
  html, body { width: 777px; height: 1200px; overflow: hidden; background: #fff; }
  .poster {
    position: relative; width: 777px; height: 1200px; overflow: hidden;
    font-family: "Nunito", sans-serif;
  }
  .scene-photo {
    position: absolute; inset: 0;
    background:
      radial-gradient(ellipse 70% 40% at 55% 62%, rgba(255,236,170,0.75), rgba(255,236,170,0) 70%),
      linear-gradient(180deg, var(--sky-top) 0%, #f5d995 35%, var(--sky-mid) 62%, #e08a2c 82%, var(--sky-low) 100%);
  }
  .runner-photo {
    position: absolute; left: 590px; top: 0; width: 187px; height: 1170px;
    background: linear-gradient(90deg, rgba(214,40,36,0) 0%, rgba(214,40,36,0.85) 22%, #cf2a2a 60%, #b8241f 100%);
    border-radius: 60% 0 0 30% / 20% 0 0 10%;
  }
  .equipment-photo {
    position: absolute; left: 0; top: 436px; width: 396px; height: 680px;
    background: linear-gradient(160deg, rgba(110,95,80,0.15) 0%, rgba(95,80,65,0.55) 45%, rgba(80,65,50,0.7) 100%);
    border-radius: 0 40% 30% 0 / 0 20% 25% 0;
  }
  .title {
    position: absolute; left: 22px; top: 12px;
    font-family: "Oswald", sans-serif; font-weight: 700;
    font-size: 74px; line-height: 77px; letter-spacing: 2px;
    text-transform: uppercase;
    color: rgba(255,255,255,0.12);
    -webkit-text-stroke: 2.5px var(--title-red);
  }
  .tagline {
    position: absolute; left: 0; top: 318px; width: 600px;
    text-align: center; color: var(--ink-blue);
    font-size: 27px; line-height: 34px; font-weight: 900;
  }
  .dates {
    position: absolute; left: 300px; top: 416px; width: 348px; height: 188px;
    background: var(--box-red);
    box-shadow: 0 0 12px 4px rgba(90,70,60,0.55);
    color: var(--sun-yellow); font-weight: 800; font-size: 19px; line-height: 24px;
    padding: 8px 19px 0 10px;
  }
  .dates dt { margin-top: 4px; }
  .dates dd { text-align: right; margin-bottom: 7px; }
  .big-six {
    position: absolute; left: 420px; top: 585px; width: 136px; text-align: center;
    font-family: "Oswald", sans-serif; font-weight: 300; font-size: 218px; line-height: 218px;
    color: transparent; -webkit-text-stroke: 2px var(--ink-blue);
  }
  .offer {
    position: absolute; left: 270px; top: 772px; width: 440px; text-align: center;
    color: var(--ink-blue); font-size: 27px; line-height: 34px; font-weight: 900;
  }
  .price {
    position: absolute; left: 330px; top: 826px; width: 320px; text-align: center;
    font-family: "Oswald", sans-serif; font-weight: 300; font-size: 200px; line-height: 200px;
    color: transparent; -webkit-text-stroke: 2.5px var(--ink-blue);
  }
  .prize { position: absolute; left: 528px; top: 948px; width: 224px; height: 224px; }
  .prize svg { position: absolute; inset: 0; }
  .prize p {
    position: absolute; inset: 0; display: flex; flex-direction: column; justify-content: center;
    text-align: center; color: var(--sun-yellow); font-size: 27px; line-height: 33px; font-weight: 800;
  }
  .info-band {
    position: absolute; left: 0; top: 1170px; width: 777px; height: 30px;
    background: var(--band-red); color: var(--white);
    text-align: center; font-size: 16px; line-height: 30px; font-weight: 800;
  }
  .info-band .site { color: var(--sun-yellow); }
</style>
</head>
<body>
<main class="poster">
  <div class="scene-photo" role="img" aria-label="Warm sunrise backdrop glowing yellow to orange"></div>
  <div class="runner-photo" role="img" aria-label="Silhouette of a woman jogging in red against the sunrise"></div>
  <div class="equipment-photo" role="img" aria-label="Elliptical trainer and iron weight plates"></div>

  <h1 class="title">Bright Dawn,<br>Bold Self<br>Reshape<br>Challenge</h1>

  <p class="tagline">In Just 6 Weeks, Transform Your Body<br>And Get In The Best Shape Of Your Life!</p>

  <dl class="dates">
    <dt>Kick Off Meeting:</dt><dd>Thursday, Jan 14 at 7:30 pm</dd>
    <dt>Start Date:</dt><dd>Monday, January 18th</dd>
    <dt>End Date:</dt><dd>Friday, February 26th</dd>
  </dl>

  <div class="big-six">6</div>
  <p class="offer">Weeks of Training, Nutrition,<br>and Coaching Starting at just</p>
  <div class="price">$99!</div>

  <div class="prize">
    <svg viewBox="0 0 224 224" width="224" height="224" aria-hidden="true">
      <polygon fill="var(--ink-blue)" points="224,112 199,135 209,168 176,176 168,209 135,199 112,224 89,199 56,209 48,176 15,168 25,135 0,112 25,89 15,56 48,48 56,15 89,25 112,0 135,25 168,15 176,48 209,56 199,89"/>
    </svg>
    <p>$500<br>CASH Prize<br>for Winner!</p>
  </div>

  <footer class="info-band">Visit <span class="site">www.vorabloombootcamps.com</span> FOR MORE INFO</footer>
</main>
</body>
</html>
```